Design a For Sale sign board and Direction Sign Board.
Attached is an example of what i am thinking but am happy to look at any options.
Colours are to be ""bright Orange"on white and in reverse as well.

Logo id Fairbrook & Co Real Estate.

```html
<!DOCTYPE html>
<html lang="en">
<head>
<meta charset="utf-8">
<title>Fairbrook &amp; Co Real Estate – Sale and Direction Boards</title>
<link rel="stylesheet" href="https://fonts.googleapis.com/css2?family=Archivo:wght@700&display=swap">
<style>
  :root {
    --orange: #f7941e;
    --white: #ffffff;
  }
  html, body {
    margin: 0;
    padding: 0;
    overflow: hidden;
    background: var(--white);
  }
  .canvas {
    position: relative;
    width: 960px;
    height: 1200px;
    overflow: hidden;
    background: var(--white);
    font-family: "Archivo", "Helvetica Neue", Arial, sans-serif;
    font-weight: 700;
  }
  .board {
    position: absolute;
    left: 130px;
    width: 700px;
    box-sizing: border-box;
    text-align: center;
  }
  .board--sale {
    top: 114px;
    height: 404px;
    border: 8px solid var(--orange);
    border-radius: 11px;
    color: var(--orange);
  }
  .board--direction {
    top: 693px;
    height: 397px;
    background: var(--orange);
    border-radius: 10px;
    color: var(--white);
  }
  .brand {
    position: absolute;
    left: 0;
    right: 0;
    line-height: 1;
  }
  .board--sale .brand { top: 62px; }
  .board--direction .brand { top: 55px; }
  .brand__name {
    display: block;
    font-size: 56px;
    letter-spacing: 0.5px;
    white-space: nowrap;
  }
  .brand__tagline {
    display: block;
    margin-top: 14px;
    font-size: 32px;
    letter-spacing: 0.5px;
  }
  .agent {
    position: absolute;
    left: 0;
    right: 0;
    margin: 0;
    font-size: 80px;
    line-height: 1;
    letter-spacing: -0.5px;
    white-space: nowrap;
  }
  .board--sale .agent { top: 234px; }
  .board--direction .agent { top: 202px; }
  .phone {
    position: absolute;
    left: 0;
    right: 0;
    top: 326px;
    margin: 0;
    font-size: 56px;
    line-height: 1;
    letter-spacing: -0.5px;
  }
  .arrow {
    position: absolute;
    left: 188px;
    top: 283px;
    width: 324px;
    height: 82px;
  }
  .arrow path { fill: var(--white); }
</style>
</head>
<body>
<main class="canvas">
  <section class="board board--sale" aria-label="For sale sign board">
    <div class="brand">
      <span class="brand__name">FAIRBROOK &amp; CO</span>
      <span class="brand__tagline">REAL ESTATE</span>
    </div>
    <p class="agent">ROB KELLER</p>
    <p class="phone">0400 318 627</p>
  </section>

  <section class="board board--direction" aria-label="Direction sign board">
    <div class="brand">
      <span class="brand__name">FAIRBROOK &amp; CO</span>
      <span class="brand__tagline">REAL ESTATE</span>
    </div>
    <p class="agent">ROB KELLER</p>
    <svg class="arrow" viewBox="0 0 324 82" aria-label="Arrow pointing left" role="img">
      <path d="M0 41 L40 0 L40 20 L324 20 L324 62 L40 62 L40 82 Z"/>
    </svg>
  </section>
</main>
</body>
</html>
```